eJuice bottle label

We need a design for a label we are putting on eJuice liquid glass bottles, I have attached what we have in mind. We are a Colorado family ran business so we are going to name our flavors after Colorado Passes and would like a picture of the pass on the bottle. There will be 5 total labels.

```html
<!DOCTYPE html>
<html lang="en">
<head>
<meta charset="utf-8">
<title>Summit Trail Craft Liquids – Timberline Label</title>
<link rel="stylesheet" href="https://fonts.googleapis.com/css2?family=Fondamento&family=Federo&family=Noto+Serif:wght@400;700&display=swap">
<style>
  :root {
    --gold-edge: #ecbb35;
    --gold-mid: #f4d97e;
    --gold-light: #fdf6de;
    --glow: #fffefa;
    --pine: #2f6a2c;
    --pine-deep: #27651f;
    --ink: #1b1508;
    --earth: #3a2916;
  }
  * { margin: 0; padding: 0; box-sizing: border-box; }
  html, body {
    width: 1200px;
    height: 497px;
    overflow: hidden;
    background: #ffffff;
  }
  .label {
    position: relative;
    width: 1200px;
    height: 497px;
    overflow: hidden;
    background: linear-gradient(90deg,
      var(--gold-edge) 0%,
      var(--gold-mid) 22%,
      var(--gold-light) 42%,
      var(--glow) 53%,
      var(--gold-light) 63%,
      var(--gold-mid) 80%,
      var(--gold-edge) 100%);
    font-family: "Noto Serif", serif;
    color: var(--ink);
  }

  /* Left warning strip */
  .warning {
    position: absolute;
    left: 40px;
    top: 16px;
    height: 466px;
    writing-mode: vertical-rl;
    font-family: "Noto Serif", serif;
    font-weight: 700;
    font-size: 13.5px;
    line-height: 16px;
    letter-spacing: 2.2px;
    text-transform: uppercase;
    color: var(--ink);
  }

  /* Company name, set straight in the label's text face */
  .company {
    position: absolute;
    left: 0;
    width: 1206px;
    top: 70px;
    text-align: center;
    font-family: "Noto Serif", serif;
    font-weight: 700;
    font-size: 28px;
    line-height: 1;
    letter-spacing: 3px;
    text-transform: uppercase;
    color: var(--pine);
  }

  /* Strength */
  .strength {
    position: absolute;
    left: 914px;
    top: 22px;
    font-family: "Noto Serif", serif;
    font-size: 28px;
    letter-spacing: 2px;
    color: var(--ink);
  }

  /* Right ingredients strip, reading bottom to top */
  .ingredients {
    position: absolute;
    left: 1088px;
    top: 14px;
    height: 468px;
    writing-mode: vertical-rl;
    transform: rotate(180deg);
    font-family: "Noto Serif", serif;
    font-size: 18.5px;
    line-height: 21px;
    letter-spacing: 2.3px;
    color: var(--ink);
  }
  .nicotine-note {
    position: absolute;
    left: 1156px;
    top: 36px;
    height: 424px;
    writing-mode: vertical-rl;
    transform: rotate(180deg);
    font-family: "Noto Serif", serif;
    font-weight: 700;
    font-size: 13.5px;
    letter-spacing: 2.6px;
    text-transform: uppercase;
    color: var(--ink);
  }

  /* Pass illustration area */
  .pass-art {
    position: absolute;
    left: 236px;
    top: 140px;
    width: 765px;
    height: 186px;
    border-radius: 90px 90px 4px 4px;
    background: linear-gradient(180deg,
      rgba(255,255,255,0.85) 0%,
      rgba(185,226,143,0.55) 55%,
      rgba(47,106,44,0.22) 100%);
  }

  /* Flavour name */
  .flavour {
    position: absolute;
    left: 0;
    width: 1206px;
    top: 374px;
    text-align: center;
    font-family: "Fondamento", serif;
    font-weight: 400;
    font-size: 56px;
    line-height: 1;
    color: var(--pine-deep);
  }
  .origin {
    position: absolute;
    left: 0;
    width: 1206px;
    top: 448px;
    text-align: center;
    font-family: "Federo", sans-serif;
    font-size: 24px;
    letter-spacing: 0.5px;
    color: var(--earth);
  }
</style>
</head>
<body>
  <main class="label">
    <p class="warning">Must be 18 years of age to purchase.product<br>may contain nicotine. keep away from<br>children and pets.</p>

    <p class="company">Summit Trail Craft Liquids</p>

    <div class="pass-art" role="img" aria-label="Illustration of three snow-capped mountain peaks drawn with green outlines, depicting the Timberline pass"></div>

    <p class="strength">3 mg</p>

    <h1 class="flavour">Timberline</h1>
    <p class="origin">Hand Crafted in Colorado</p>

    <p class="ingredients">Ingredients: USP Vegetable glycerin,<br>USP Propylene glycol, Natural/Artificial<br>Flavourines.</p>
    <p class="nicotine-note">May conatin vapinegrade USP nicotine.</p>
  </main>
</body>
</html>
```